The Marisol & Jocelyn Fruit Co.

We produce a very high quality freeze dried fruit, all organic, no preservative, no additives, nothing but the fruit. To get more use out of a facility we have in Charlotte, we decided to pursue some high end online retailers with a high end freeze dried organic fruit. We are looking for a very high end, upper east side, trendy, hip, logo and package design for this. There are 4 SKU's - Freeze Dried Strawberries, Freeze Dried Blueberries, Freeze Dried Cherries, and a blend of of all 3 as the 4th SKU. 2 labels each that are 6" x 6" - The front, again needs to be fun and trendy big bold etc. Nothing frilly and Quiet Barn by the creek. The back needs to contain the nutritional statements for each and some copy describing the product and the company.
Updates
This would be one of only a few competitors in this segment
We are looking to steal a page from the wine industry. The coolest looking label on the shelf wins over the uneducated wine buyer. The designs are all fine, but they need to be sleeker, sexier, funner, etc. Someone should look at the label and say....wow that is FUN AND SEXY! I have to buy some! VORBEX.COM screams that. Don't worry so much about pictures of the fruit as the bag is going to be clear. Sell the brand not the fruit. OK?
Reason: Why not?
Reason: Final Selection by Monday 5pm EST.
For all designs that have not been eliminated:
Reason: Final selections. All four designs front and back on one file uploaded by noon tomorrow ( 12:01 PM EST New York)
Target Market(s)
People that would shop at sites like www.vorbex.com
Industry/Entity Type
It Company
Requirements
Nice to have
- The brand is named after our two daughters - One is very girly and the other is very "sassy" It would be fun to have the logo capture their personalities a little. I have uploaded a picture. Marisol on the left, Jocelyn on the right.
Also, another of our brands, Hank Pellow, packaging is attached here. Some consistency in look and feel may be good.
Should not have
- Nothing frilly or dainty, or delicate. Colorful fun and bold but trendy.

```html
<!DOCTYPE html>
<html lang="en">
<head>
<meta charset="utf-8">
<title>The Marisol &amp; Jocelyn Fruit Co. — Freeze Dried Fruit Labels</title>
<link rel="stylesheet" href="https://fonts.googleapis.com/css2?family=Bodoni+Moda:wght@400;500&family=Montserrat:wght@500;600;700&family=Roboto+Condensed:wght@400;700&display=swap">
<style>
  :root {
    --page: #ffffff;
    --topbar: #3a3a3a;
    --ink: #ffffff;
    --strawberry: #e8383a;
    --strawberry-deep: #d9262c;
    --cherry: #8a1a36;
    --cherry-deep: #731229;
    --blueberry: #231a3d;
    --blueberry-deep: #1b1332;
    --lime: #8dc63f;
    --rose: #e8327c;
    --tangerine: #f7941d;
    --midnight: #231a3d;
  }
  * { box-sizing: border-box; margin: 0; padding: 0; }
  html, body { width: 1200px; height: 1000px; overflow: hidden; background: var(--page); }
  .canvas { position: relative; width: 1200px; height: 1000px; }
  .topbar { position: absolute; left: 0; top: 0; width: 1200px; height: 8px; background: var(--topbar); }

  .label {
    position: absolute; width: 257px; height: 258px;
    border: 5px solid; border-radius: 15px; overflow: hidden;
    color: var(--ink);
  }
  .row-front { top: 205px; }
  .row-back { top: 480px; }
  .col-1 { left: 53px; } .col-2 { left: 333px; } .col-3 { left: 612px; } .col-4 { left: 890px; }

  .sku-strawberry { background: var(--strawberry); border-color: var(--lime); }
  .sku-cherry { background: var(--cherry); border-color: var(--rose); }
  .sku-blueberry { background: var(--blueberry); border-color: var(--tangerine); }
  .sku-blend-front { background: var(--midnight); border-color: var(--midnight); }
  .sku-blend-back { background: var(--strawberry); border-color: var(--midnight); }

  .sheen { position: absolute; inset: 0; }
  .sku-strawberry .sheen { background: radial-gradient(ellipse 120% 60% at 20% 25%, rgba(255,255,255,.10), transparent 60%), linear-gradient(160deg, transparent 40%, var(--strawberry-deep) 100%); }
  .sku-cherry .sheen { background: radial-gradient(ellipse 120% 60% at 20% 25%, rgba(255,255,255,.08), transparent 60%), linear-gradient(160deg, transparent 40%, var(--cherry-deep) 100%); }
  .sku-blueberry .sheen { background: radial-gradient(ellipse 120% 60% at 20% 25%, rgba(120,80,170,.25), transparent 60%), linear-gradient(160deg, transparent 40%, var(--blueberry-deep) 100%); }
  .blend-pattern {
    position: absolute; inset: 0;
    background: linear-gradient(125deg, var(--midnight) 0 18%, var(--strawberry) 18% 38%, var(--cherry) 38% 52%, var(--strawberry) 52% 70%, var(--midnight) 70% 82%, var(--strawberry) 82%);
    opacity: .95;
  }

  .brand {
    position: absolute; left: 14px; top: 14px; width: 222px;
    font-family: "Montserrat", sans-serif; font-weight: 600; text-transform: uppercase; color: var(--ink);
  }
  .brand-the { display: block; font-size: 9px; line-height: 10px; letter-spacing: 1px; }
  .brand-name { display: block; font-size: 14.5px; line-height: 16px; letter-spacing: .6px; white-space: nowrap; }
  .brand-tail { display: block; text-align: right; font-size: 8px; line-height: 10px; letter-spacing: 1px; }

  .product { position: absolute; left: 0; right: 0; top: 103px; text-align: center; }
  .product-kind { font-family: "Bodoni Moda", serif; font-size: 15px; letter-spacing: 1.5px; line-height: 17px; }
  .product-name { font-family: "Montserrat", sans-serif; font-weight: 700; font-size: 14px; letter-spacing: 2px; line-height: 15px; }
  .product-dash { width: 5px; height: 1px; background: var(--ink); margin: 4px auto 5px; }
  .product-claim { font-family: "Montserrat", sans-serif; font-weight: 600; font-size: 9.5px; letter-spacing: .8px; }

  .weight-front {
    position: absolute; left: 98px; bottom: 6px; width: 70px; text-align: center;
    font-family: "Montserrat", sans-serif; font-weight: 500; font-size: 15px;
    border-bottom: 1px solid var(--ink); line-height: 15px; padding-bottom: 1px;
  }

  .back-mark { position: absolute; left: 9px; top: 9px; width: 26px; height: 26px; border-radius: 50%; background: var(--ink); }
  .story {
    position: absolute; left: 9px; top: 41px; width: 100px;
    font-family: "Bodoni Moda", serif; font-size: 10.4px; line-height: 10.2px;
    letter-spacing: -.15px; white-space: nowrap;
  }
  .story .dash { display: block; height: 10.2px; }
  .weight-back {
    position: absolute; left: 9px; bottom: 4px;
    font-family: "Montserrat", sans-serif; font-weight: 600; font-size: 14px; line-height: 15px;
  }
  .divider { position: absolute; left: 110px; top: 10px; bottom: 12px; width: 1px; background: var(--ink); }

  .nutrition {
    position: absolute; left: 117px; top: 7px; width: 118px;
    border: 1px solid var(--ink); padding: 1px 3px 2px;
    font-family: "Roboto Condensed", sans-serif; font-size: 5px; line-height: 6px;
  }
  .sku-blend-back .nutrition { top: 9px; font-size: 5.5px; line-height: 7.4px; }
  .nutrition h3 { font-weight: 700; font-size: 16px; line-height: 15px; letter-spacing: -.3px; }
  .sku-blend-back .nutrition h3 { font-size: 17px; line-height: 17px; }
  .nf-row { display: flex; justify-content: space-between; border-bottom: .5px solid var(--ink); }
  .nf-row.indent { padding-left: 5px; }
  .nf-row b { font-weight: 700; }
  .nf-bar { height: 4px; background: var(--ink); margin: 1px 0; }
  .nf-bar.thin { height: 2px; }
  .nf-right { justify-content: flex-end; }
  .nf-note { font-size: 4px; line-height: 4.6px; padding: 1px 0; border-bottom: .5px solid var(--ink); }
  .sku-blend-back .nf-note { font-size: 4.5px; line-height: 5.4px; border-bottom: 0; }
  .nf-grid { display: grid; grid-template-columns: 30% 22% 24% 24%; font-size: 4px; line-height: 4.6px; padding-top: 1px; border-bottom: .5px solid var(--ink); }
  .nf-gram { font-size: 4px; line-height: 4.6px; padding-top: 1px; }
  .nf-gram span { display: flex; justify-content: space-between; }
  .nf-blank { height: 8px; background: var(--ink); margin-top: 2px; }
</style>
</head>
<body>
<div class="canvas">
  <div class="topbar"></div>

  <!-- Front labels -->
  <section class="label row-front col-1 sku-strawberry">
    <div class="sheen"></div>
    <div class="brand"><span class="brand-the">The</span><span class="brand-name">Marisol &amp; Jocelyn</span><span class="brand-tail">Fruit Co.</span></div>
    <div class="product">
      <div class="product-kind">Freeze Dried</div>
      <div class="product-name">STRAWBERRIES</div>
      <div class="product-dash"></div>
      <div class="product-claim">100% ORGANIC</div>
    </div>
    <div class="weight-front">1 oz.</div>
  </section>

  <section class="label row-front col-2 sku-cherry">
    <div class="sheen"></div>
    <div class="brand"><span class="brand-the">The</span><span class="brand-name">Marisol &amp; Jocelyn</span><span class="brand-tail">Fruit Co.</span></div>
    <div class="product">
      <div class="product-kind">Freeze Dried</div>
      <div class="product-name">CHERRIES</div>
      <div class="product-dash"></div>
      <div class="product-claim">100% ORGANIC</div>
    </div>
    <div class="weight-front">1 oz.</div>
  </section>

  <section class="label row-front col-3 sku-blueberry">
    <div class="sheen"></div>
    <div class="brand"><span class="brand-the">The</span><span class="brand-name">Marisol &amp; Jocelyn</span><span class="brand-tail">Fruit Co.</span></div>
    <div class="product">
      <div class="product-kind">Freeze Dried</div>
      <div class="product-name">BLUEBERRIES</div>
      <div class="product-dash"></div>
      <div class="product-claim">100% ORGANIC</div>
    </div>
    <div class="weight-front">1 oz.</div>
  </section>

  <section class="label row-front col-4 sku-blend-front">
    <div class="blend-pattern" role="img" aria-label="Angular geometric pattern in red, cherry and midnight tones"></div>
    <div class="brand"><span class="brand-the">The</span><span class="brand-name">Marisol &amp; Jocelyn</span><span class="brand-tail">Fruit Co.</span></div>
    <div class="product">
      <div class="product-kind">Freeze Dried</div>
      <div class="product-name">STRAWBERRIES<br>CHERRIES<br>BLUEBERRIES</div>
      <div class="product-dash"></div>
      <div class="product-claim">100% ORGANIC</div>
    </div>
    <div class="weight-front">1 oz.</div>
  </section>

  <!-- Back labels -->
  <section class="label row-back col-1 sku-strawberry">
    <div class="back-mark"></div>
    <div class="story">
      <span class="dash">-</span>
      <p>Lorem ipsum dolor<br>sit amet, consecte-<br>tur adipisicing elit,<br>sed do eiusmod<br>tempor incididunt<br>ut labore et dolore<br>magna aliqua. Ut<br>enim ad minim<br>veniam, quis.</p>
      <span class="dash">-</span>
      <p>Excepteur sint<br>occaecat cupidatat<br>non proident, sunt<br>in culpa qui officia<br>deserunt mollit<br>anim id est labo-<br>rum.</p>
    </div>
    <div class="weight-back">1 oz.</div>
    <div class="divider"></div>
    <div class="nutrition">
      <h3>Nutrition Facts</h3>
      <div>Serving Size 1 ounce 28g (1 ounce (28g))</div>
      <div>Servings per container 1</div>
      <div class="nf-bar"></div>
      <div class="nf-row"><b>Amount Per Serving</b></div>
      <div class="nf-row"><span><b>Calories</b> 9</span><span>Calories from Fat 1</span></div>
      <div class="nf-bar thin"></div>
      <div class="nf-row nf-right"><b>% Daily Value*</b></div>
      <div class="nf-row"><span><b>Total Fat</b> 0g</span><span>0%</span></div>
      <div class="nf-row indent"><span>Saturated Fat 0g</span><span>0%</span></div>
      <div class="nf-row indent"><span>Trans Fat</span></div>
      <div class="nf-row"><span><b>Cholesterol</b> 0mg</span><span>0%</span></div>
      <div class="nf-row"><span><b>Sodium</b> 0mg</span><span>0%</span></div>
      <div class="nf-row"><span><b>Total Carbohydrate</b> 2g</span><span>1%</span></div>
      <div class="nf-row indent"><span>Dietary Fiber 1g</span><span>2%</span></div>
      <div class="nf-row indent"><span>Sugars 1g</span></div>
      <div class="nf-row"><span><b>Protein</b> 0g</span></div>
      <div class="nf-bar"></div>
      <div class="nf-row"><span>Vitamin A &nbsp; 0% • Vitamin C</span><span>27%</span></div>
      <div class="nf-row"><span>Calcium &nbsp; 0% • Iron</span><span>1%</span></div>
      <div class="nf-note">*Percent Daily Values are based on a 2,000 calorie diet. Your daily values may be higher or lower depending on your calorie needs.</div>
      <div class="nf-grid"><span></span><span>Calories</span><span>2,000</span><span>2,500</span><span>Total Fat</span><span>Less than</span><span>65g</span><span>80g</span><span>Sat Fat</span><span>Less than</span><span>20g</span><span>25g</span><span>Cholesterol</span><span>Less than</span><span>300mg</span><span>300mg</span><span>Sodium</span><span>Less than</span><span>2,400mg</span><span>2,400mg</span><span>Total Carb.</span><span></span><span>300g</span><span>375g</span><span>Fiber</span><span></span><span>25g</span><span>30g</span></div>
      <div class="nf-gram">Calories per gram:<span><i>Fat 9</i><i>•</i><i>Carbohydrate 4</i><i>•</i><i>Protein 4</i></span></div>
    </div>
  </section>

  <section class="label row-back col-2 sku-cherry">
    <div class="back-mark"></div>
    <div class="story">
      <span class="dash">-</span>
      <p>Lorem ipsum dolor<br>sit amet, consecte-<br>tur adipisicing elit,<br>sed do eiusmod<br>tempor incididunt<br>ut labore et dolore<br>magna aliqua. Ut<br>enim ad minim<br>veniam, quis.</p>
      <span class="dash">-</span>
      <p>Excepteur sint<br>occaecat cupidatat<br>non proident, sunt<br>in culpa qui officia<br>deserunt mollit<br>anim id est labo-<br>rum.</p>
    </div>
    <div class="weight-back">1 oz.</div>
    <div class="divider"></div>
    <div class="nutrition">
      <h3>Nutrition Facts</h3>
      <div>Serving Size 1 ounce 28g (1 ounce (28g))</div>
      <div>Servings per container 1</div>
      <div class="nf-bar"></div>
      <div class="nf-row"><b>Amount Per Serving</b></div>
      <div class="nf-row"><span><b>Calories</b> 18</span><span>Calories from Fat 0</span></div>
      <div class="nf-bar thin"></div>
      <div class="nf-row nf-right"><b>% Daily Value*</b></div>
      <div class="nf-row"><span><b>Total Fat</b> 0g</span><span>0%</span></div>
      <div class="nf-row indent"><span>Saturated Fat 0g</span><span>0%</span></div>
      <div class="nf-row indent"><span>Trans Fat</span></div>
      <div class="nf-row"><span><b>Cholesterol</b> 0mg</span><span>0%</span></div>
      <div class="nf-row"><span><b>Sodium</b> 0mg</span><span>0%</span></div>
      <div class="nf-row"><span><b>Total Carbohydrate</b> 4g</span><span>1%</span></div>
      <div class="nf-row indent"><span>Dietary Fiber 1g</span><span>2%</span></div>
      <div class="nf-row indent"><span>Sugars 4g</span></div>
      <div class="nf-row"><span><b>Protein</b> 0g</span></div>
      <div class="nf-bar"></div>
      <div class="nf-row"><span>Vitamin A &nbsp; 0% • Vitamin C</span><span>3%</span></div>
      <div class="nf-row"><span>Calcium &nbsp; 0% • Iron</span><span>1%</span></div>
      <div class="nf-note">*Percent Daily Values are based on a 2,000 calorie diet. Your daily values may be higher or lower depending on your calorie needs.</div>
      <div class="nf-grid"><span></span><span>Calories</span><span>2,000</span><span>2,500</span><span>Total Fat</span><span>Less than</span><span>65g</span><span>80g</span><span>Sat Fat</span><span>Less than</span><span>20g</span><span>25g</span><span>Cholesterol</span><span>Less than</span><span>300mg</span><span>300mg</span><span>Sodium</span><span>Less than</span><span>2,400mg</span><span>2,400mg</span><span>Total Carb.</span><span></span><span>300g</span><span>375g</span><span>Fiber</span><span></span><span>25g</span><span>30g</span></div>
      <div class="nf-gram">Calories per gram:<span><i>Fat 9</i><i>•</i><i>Carbohydrate 4</i><i>•</i><i>Protein 4</i></span></div>
    </div>
  </section>

  <section class="label row-back col-3 sku-blueberry">
    <div class="back-mark"></div>
    <div class="story">
      <span class="dash">-</span>
      <p>Lorem ipsum dolor<br>sit amet, consecte-<br>tur adipisicing elit,<br>sed do eiusmod<br>tempor incididunt<br>ut labore et dolore<br>magna aliqua. Ut<br>enim ad minim<br>veniam, quis.</p>
      <span class="dash">-</span>
      <p>Excepteur sint<br>occaecat cupidatat<br>non proident, sunt<br>in culpa qui officia<br>deserunt mollit<br>anim id est labo-<br>rum.</p>
    </div>
    <div class="weight-back">1 oz.</div>
    <div class="divider"></div>
    <div class="nutrition">
      <h3>Nutrition Facts</h3>
      <div>Serving Size 1 ounce 28g (1 ounce (28g))</div>
      <div>Servings per container 1</div>
      <div class="nf-bar"></div>
      <div class="nf-row"><b>Amount Per Serving</b></div>
      <div class="nf-row"><span><b>Calories</b> 18</span><span>Calories from Fat 1</span></div>
      <div class="nf-bar thin"></div>
      <div class="nf-row nf-right"><b>% Daily Value*</b></div>
      <div class="nf-row"><span><b>Total Fat</b> 0g</span><span>0%</span></div>
      <div class="nf-row indent"><span>Saturated Fat 0g</span><span>0%</span></div>
      <div class="nf-row indent"><span>Trans Fat</span></div>
      <div class="nf-row"><span><b>Cholesterol</b> 0mg</span><span>0%</span></div>
      <div class="nf-row"><span><b>Sodium</b> 0mg</span><span>0%</span></div>
      <div class="nf-row"><span><b>Total Carbohydrate</b> 4g</span><span>1%</span></div>
      <div class="nf-row indent"><span>Dietary Fiber 1g</span><span>3%</span></div>
      <div class="nf-row indent"><span>Sugars 3g</span></div>
      <div class="nf-row"><span><b>Protein</b> 0g</span></div>
      <div class="nf-bar"></div>
      <div class="nf-row"><span>Vitamin A &nbsp; 0% • Vitamin C</span><span>5%</span></div>
      <div class="nf-row"><span>Calcium &nbsp; 0% • Iron</span><span>0%</span></div>
      <div class="nf-note">*Percent Daily Values are based on a 2,000 calorie diet. Your daily values may be higher or lower depending on your calorie needs.</div>
      <div class="nf-grid"><span></span><span>Calories</span><span>2,000</span><span>2,500</span><span>Total Fat</span><span>Less than</span><span>65g</span><span>80g</span><span>Sat Fat</span><span>Less than</span><span>20g</span><span>25g</span><span>Cholesterol</span><span>Less than</span><span>300mg</span><span>300mg</span><span>Sodium</span><span>Less than</span><span>2,400mg</span><span>2,400mg</span><span>Total Carb.</span><span></span><span>300g</span><span>375g</span><span>Fiber</span><span></span><span>25g</span><span>30g</span></div>
      <div class="nf-gram">Calories per gram:<span><i>Fat 9</i><i>•</i><i>Carbohydrate 4</i><i>•</i><i>Protein 4</i></span></div>
    </div>
  </section>

  <section class="label row-back col-4 sku-blend-back">
    <div class="back-mark"></div>
    <div class="story">
      <span class="dash">-</span>
      <p>Lorem ipsum dolor<br>sit amet, consecte-<br>tur adipisicing elit,<br>sed do eiusmod<br>tempor incididunt<br>ut labore et dolore<br>magna aliqua. Ut<br>enim ad minim<br>veniam, quis.</p>
      <span class="dash">-</span>
      <p>Excepteur sint<br>occaecat cupidatat<br>non proident, sunt<br>in culpa qui officia<br>deserunt mollit<br>anim id est labo-<br>rum.</p>
    </div>
    <div class="weight-back">1 oz.</div>
    <div class="divider"></div>
    <div class="nutrition">
      <h3>Nutrition Facts</h3>
      <div>Serving Size 1 ounce 28g (1 ounce (28g))</div>
      <div>Servings per container 1</div>
      <div class="nf-bar"></div>
      <div class="nf-row"><b>Amount Per Serving</b></div>
      <div class="nf-row"><span><b>Calories</b> 12</span><span>Calories from Fat 1</span></div>
      <div class="nf-bar thin"></div>
      <div class="nf-row nf-right"><b>% Daily Value*</b></div>
      <div class="nf-row"><span><b>Total Fat</b> 0g</span><span>0%</span></div>
      <div class="nf-row indent"><span>Saturated Fat 0g</span><span>0%</span></div>
      <div class="nf-row indent"><span>Trans Fat</span></div>
      <div class="nf-row"><span><b>Cholesterol</b> 0mg</span><span>0%</span></div>
      <div class="nf-row"><span><b>Sodium</b> 0mg</span><span>0%</span></div>
      <div class="nf-row"><span><b>Total Carbohydrate</b> 3g</span><span>1%</span></div>
      <div class="nf-row indent"><span>Dietary Fiber 1g</span><span>6%</span></div>
      <div class="nf-row indent"><span>Sugars 1g</span></div>
      <div class="nf-row"><span><b>Protein</b> 0g</span></div>
      <div class="nf-bar"></div>
      <div class="nf-row"><span>Vitamin A &nbsp; 1% • Vitamin C</span><span>10%</span></div>
      <div class="nf-row"><span>Calcium &nbsp; 1% • Iron</span><span>1%</span></div>
      <div class="nf-note">*Percent Daily Values are based on a 2,000 calorie diet. Your daily values may be higher or lower depending on your calorie needs.</div>
      <div class="nf-blank"></div>
    </div>
  </section>
</div>
</body>
</html>
```